Business cards for a tribute and obituary website

Our website is called Quiet Orchard.

It is a special place online for people to remember their loved ones who have passed away, through obituaries and tributes. Friends and family can also convey their condolences on the deceased's memorial page. Celebrating the life of the deceased and remembering their legacy is very important to us – death should not be just about grieving.

We would like the card to look tasteful and modern. The design should ideally not have colours that are too bright. The logo and website URL, www.quietorchardpages.net should be visible on the front of the card, with our slogan "Honouring every story told" on the back.

The design should communicate our purpose – remembering loved ones who have passed – and also a lighter tone of celebrating life. It should not look like a funeral director's card!

Our logo has been attached. Looking forward to some beautiful designs! Get creative :)
Updates

Reason: Thank you all for your designs. The rest of my team and I have not reached a decision on which design to select and I am collecting feedback from them. I will provide feedback for any changes that need to be made soon. It would be great if we could see more original designs and in more colours! We will definitely select a design by this deadline.

Industry/Entity Type

Business

Contact Information for Business Card

Nadia Fenwick
Project Manager
471226809
nadiafenwick@quietorchardpages.net

Font styles to use
Serif
Sans Serif

Requirements
Must have
• Logo and website address (www.quietorchardpages.net) on the front.
Nice to have
• Hi designers! It would be nice to see alternative colours – feel free to try out colours that are tasteful and subtle. The colour of the business card does not have to be the same as the logo.
• We would also like to see the logo used in different ways, perhaps a glossy or embossed finish. The card should look stylish.

```html
<!DOCTYPE html>
<html lang="en">
<head>
<meta charset="utf-8">
<title>Quiet Orchard – Business Cards</title>
<link rel="stylesheet" href="https://fonts.googleapis.com/css2?family=Lato:wght@300;400&family=Roboto+Slab:wght@300;400;700&display=swap">
<style>
  :root {
    --backdrop: #e8e6e2;
    --sage: #8da23b;
    --navy: #163c5d;
    --ink-light: #ffffff;
    --ink-soft: rgba(255, 255, 255, 0.88);
    --gold: #d8c46a;
  }
  * { box-sizing: border-box; margin: 0; padding: 0; }
  html, body {
    width: 1200px;
    height: 873px;
    overflow: hidden;
    background: var(--backdrop);
  }
  .canvas {
    position: relative;
    width: 1200px;
    height: 873px;
  }
  .card {
    position: absolute;
    top: 288px;
    width: 520px;
    height: 297px;
    border-radius: 3px;
    overflow: hidden;
    box-shadow: 0 2px 10px rgba(0, 0, 0, 0.12);
  }

  /* Contact side */
  .card--contact {
    left: 50px;
    background: var(--sage);
    color: var(--ink-light);
  }
  .contact-block {
    position: absolute;
    left: 40px;
    top: 38px;
  }
  .holder-name {
    font-family: "Roboto Slab", serif;
    font-weight: 300;
    font-size: 34px;
    line-height: 1;
    letter-spacing: 0.3px;
  }
  .holder-rule {
    width: 220px;
    height: 1px;
    background: var(--ink-soft);
    margin: 8px 0 6px;
  }
  .holder-role {
    font-family: "Lato", sans-serif;
    font-weight: 300;
    font-size: 13px;
    letter-spacing: 0.6px;
    color: var(--ink-soft);
    margin-bottom: 14px;
  }
  .contact-line {
    display: flex;
    align-items: center;
    gap: 9px;
    font-family: "Lato", sans-serif;
    font-weight: 300;
    font-size: 17px;
    margin-bottom: 6px;
  }
  .contact-icon {
    width: 16px;
    height: 16px;
    flex: none;
  }

  /* Brand side */
  .card--brand {
    left: 630px;
    background: var(--navy);
    color: var(--ink-light);
  }
  .brand-lockup {
    position: absolute;
    left: 52px;
    top: 70px;
    display: flex;
    align-items: center;
    gap: 20px;
  }
  .brand-dot {
    width: 62px;
    height: 62px;
    border-radius: 50%;
    background: var(--ink-light);
    flex: none;
  }
  .brand-name {
    font-family: "Roboto Slab", serif;
    font-weight: 700;
    font-size: 44px;
    line-height: 1;
  }
  .brand-slogan {
    position: absolute;
    left: 134px;
    top: 138px;
    font-family: "Roboto Slab", serif;
    font-weight: 400;
    font-size: 17px;
    color: var(--ink-light);
  }
  .brand-url {
    position: absolute;
    left: 52px;
    bottom: 40px;
    font-family: "Roboto Slab", serif;
    font-weight: 400;
    font-size: 18px;
    letter-spacing: 0.4px;
    color: var(--gold);
  }
</style>
</head>
<body>
<main class="canvas">
  <section class="card card--contact" aria-label="Business card, contact side">
    <div class="contact-block">
      <h1 class="holder-name">Nadia Fenwick</h1>
      <div class="holder-rule"></div>
      <p class="holder-role">Project Manager</p>
      <p class="contact-line">
        <svg class="contact-icon" viewBox="0 0 16 16" aria-hidden="true">
          <circle cx="8" cy="8" r="8" fill="#ffffff"/>
          <path d="M5.3 4.2l1.3 1.6-.7 1c.5 1.1 1.3 1.9 2.4 2.4l1-.7 1.6 1.3-.8 1.2C7.7 11 5 8.3 4.1 5z" fill="#8da23b"/>
        </svg>
        471226809
      </p>
      <p class="contact-line">
        <svg class="contact-icon" viewBox="0 0 16 16" aria-hidden="true">
          <circle cx="8" cy="8" r="8" fill="#ffffff"/>
          <rect x="4" y="5.2" width="8" height="5.6" rx="0.6" fill="#8da23b"/>
          <path d="M4.3 5.6L8 8.4l3.7-2.8" fill="none" stroke="#ffffff" stroke-width="0.8"/>
        </svg>
        nadiafenwick@quietorchardpages.net
      </p>
    </div>
  </section>

  <section class="card card--brand" aria-label="Business card, brand side">
    <div class="brand-lockup">
      <div class="brand-dot"></div>
      <h2 class="brand-name">Quiet Orchard</h2>
    </div>
    <p class="brand-slogan">Honouring every story told</p>
    <p class="brand-url">www.quietorchardpages.net</p>
  </section>
</main>
</body>
</html>
```